Rock climbing centre flyer

We need a general flyer for our rock climbing gym that we can use for general advertising inside and outside the gym.

Target Market(s)

Fitness enthusiasts, dare devils, people willing to try something different

Industry/Entity Type

Fitness

Font styles to use
Other font styles liked:
• Any kind of distressed font

Colors
cadf82
eaf2ce
e9e9e9
474747

Requirements
Must have
• Double sided flyer
• Main tag line should be "No strings attached"
• Ferro Ascent logo
• Large imagery
• Address: 7/41 Wexley Road South Tarrinbee
• Phone: 9417 5836
• Email: info@ferroascent.example.com.au
• Opening hours (find from the website ferroascent.example.com.au)
• List our services:
• Unlimited bouldering
• Strength & Conditioning
• Yoga
• Birthday parties & group activities
• Kids coaching and specialist technique training
• View our timetable online at ferroascent.example.com.au
• Find us on Facebook Ferro Ascent Centre

```html
<!DOCTYPE html>
<html lang="en">
<head>
<meta charset="utf-8">
<title>Ferro Ascent – Flyer</title>
<link rel="stylesheet" href="https://fonts.googleapis.com/css2?family=Black+Ops+One&family=Bebas+Neue&family=Roboto+Condensed:wght@400;700&family=Roboto+Slab:wght@400&display=swap">
<style>
  :root{
    --lime:#cadf82;
    --lime-strong:#b5cc3f;
    --pale:#eaf2ce;
    --light:#e9e9e9;
    --charcoal:#474747;
    --ink:#1e1e1e;
    --stage:#2c2c2c;
  }
  *{margin:0;padding:0;box-sizing:border-box}
  html,body{width:1200px;height:881px;overflow:hidden;background:var(--stage)}
  .canvas{position:relative;width:1200px;height:881px}
  .flyer{position:absolute;width:518px;height:668px;background:var(--charcoal);overflow:hidden;font-family:"Roboto Condensed",sans-serif}
  .flyer--front{left:51px;top:71px}
  .flyer--back{left:608px;top:128px;width:516px}
  .shapes{position:absolute;inset:0}
  .photo{position:absolute}

  .front-hero{left:0;top:0;width:518px;height:317px;
    clip-path:polygon(0 0,100% 0,100% 80%,70% 100%,0 100%);
    background:linear-gradient(160deg,#6f9a5a 0%,#b9c85a 30%,#5fa8c8 48%,#6a6455 62%,#4a463e 100%)}
  .front-side{left:0;top:360px;width:203px;height:308px;
    background:linear-gradient(170deg,#b9b9b6 0%,#8e8d88 45%,#d7d4c9 70%,#6f6e69 100%)}
  .back-hero{left:0;top:0;width:516px;height:530px;
    background:linear-gradient(150deg,#b7b7a8 0%,#9aa35a 30%,#8a8a84 55%,#c2c0ba 80%,#7b7a76 100%)}

  .tagline{position:absolute;font-family:"Black Ops One",sans-serif;color:var(--ink);font-size:29px;letter-spacing:1px;white-space:nowrap}
  .brand{position:absolute;font-family:"Bebas Neue",sans-serif;white-space:nowrap;line-height:1}

  .hours{position:absolute;right:13px;top:288px;text-align:right;color:#f1f1f1;font-family:Arial,sans-serif;font-size:8.5px;line-height:10px}
  .hours__title{font-family:"Black Ops One",sans-serif;color:var(--lime);font-size:13px;line-height:16px;letter-spacing:.5px}
  .hours__day{font-weight:700}

  .services{position:absolute;left:219px;top:438px}
  .services__title{font-family:"Black Ops One",sans-serif;color:var(--lime);font-size:17px;margin-bottom:10px}
  .services__list{list-style:none}
  .services__item{display:flex;align-items:center;gap:9px;color:#e6e6e6;font-size:15px;height:20px}
  .services__icon{width:11px;height:11px;flex:none}

  .contact-front{position:absolute;right:13px;top:592px;text-align:right;font-family:"Roboto Slab",serif;font-size:14px;line-height:16px;color:var(--ink)}
  .web-front{position:absolute;left:224px;top:630px;font-family:"Roboto Condensed",sans-serif;font-weight:700;font-size:15px;color:var(--ink);letter-spacing:.2px}

  .social{position:absolute;right:11px;top:508px;display:flex;flex-direction:column;align-items:flex-end;gap:9px}
  .social__dot{width:22px;height:22px;border-radius:50%;background:var(--lime-strong);margin-right:6px}
  .social__name{color:var(--lime);font-size:14px}
  .address{position:absolute;left:0;right:0;top:588px;text-align:center;color:var(--light);font-size:14px;line-height:19px}
  .web-bar{position:absolute;left:101px;top:637px;width:308px;height:20px;background:var(--lime-strong);text-align:center;font-weight:700;font-size:15px;line-height:20px;color:var(--ink);letter-spacing:1px}
</style>
</head>
<body>
<main class="canvas">

  <!-- Front side -->
  <section class="flyer flyer--front">
    <svg class="shapes" width="518" height="668" viewBox="0 0 518 668" aria-hidden="true">
      <polygon points="0,317 362,317 303,351 0,351" fill="var(--lime-strong)"/>
      <polygon points="203,583 518,583 518,668" fill="var(--lime-strong)"/>
      <polygon points="203,572 518,668 203,668" fill="#ffffff"/>
      <polygon points="0,610 165,668 0,668" fill="var(--lime-strong)"/>
      <line x1="203" y1="405" x2="370" y2="351" stroke="#bdbdbd" stroke-width="1"/>
    </svg>
    <div class="photo front-hero" role="img" aria-label="Climber hanging beneath an overhanging bouldering wall covered in colourful holds"></div>
    <div class="photo front-side" role="img" aria-label="Climber reaching for a hold on a grey bouldering wall"></div>
    <polygon></polygon>
    <div class="tagline" style="left:14px;top:314px">NO STRINGS ATTACHED</div>
    <div class="hours">
      <div class="hours__title">OPENING HOURS</div>
      <div class="hours__day">MONDAY - FRIDAY</div>
      <div>4:30pm - 10:00pm</div>
      <div class="hours__day">SATURDAY - SUNDAY</div>
      <div>12:00nn - 8:00pm</div>
    </div>
    <div class="brand" style="right:13px;top:368px;font-size:44px;color:var(--light)">FERRO ASCENT</div>
    <div class="services">
      <h2 class="services__title">OUR SERVICES:</h2>
      <ul class="services__list">
        <li class="services__item"><svg class="services__icon" viewBox="0 0 12 12"><circle cx="6" cy="6" r="5" fill="none" stroke="var(--lime)" stroke-width="1.4"/><path d="M5 3.5 7.5 6 5 8.5" fill="none" stroke="var(--lime)" stroke-width="1.4"/></svg>Unlimited bouldering</li>
        <li class="services__item"><svg class="services__icon" viewBox="0 0 12 12"><circle cx="6" cy="6" r="5" fill="none" stroke="var(--lime)" stroke-width="1.4"/><path d="M5 3.5 7.5 6 5 8.5" fill="none" stroke="var(--lime)" stroke-width="1.4"/></svg>Strength &amp; Conditioning</li>
        <li class="services__item"><svg class="services__icon" viewBox="0 0 12 12"><circle cx="6" cy="6" r="5" fill="none" stroke="var(--lime)" stroke-width="1.4"/><path d="M5 3.5 7.5 6 5 8.5" fill="none" stroke="var(--lime)" stroke-width="1.4"/></svg>Yoga</li>
        <li class="services__item"><svg class="services__icon" viewBox="0 0 12 12"><circle cx="6" cy="6" r="5" fill="none" stroke="var(--lime)" stroke-width="1.4"/><path d="M5 3.5 7.5 6 5 8.5" fill="none" stroke="var(--lime)" stroke-width="1.4"/></svg>Birthday parties &amp; group activities</li>
        <li class="services__item"><svg class="services__icon" viewBox="0 0 12 12"><circle cx="6" cy="6" r="5" fill="none" stroke="var(--lime)" stroke-width="1.4"/><path d="M5 3.5 7.5 6 5 8.5" fill="none" stroke="var(--lime)" stroke-width="1.4"/></svg>Kids coaching and specialist technique training</li>
      </ul>
    </div>
    <div class="contact-front">Get in touch<br>9417 5836</div>
    <div class="web-front">WWW.FERROASCENT.EXAMPLE.COM.AU</div>
  </section>

  <!-- Back side -->
  <section class="flyer flyer--back">
    <div class="photo back-hero" role="img" aria-label="Climber in a green shirt scaling a grey bouldering wall with colourful holds"></div>
    <svg class="shapes" width="516" height="668" viewBox="0 0 516 668" aria-hidden="true">
      <polygon points="0,323 431,530 0,530" fill="var(--pale)" opacity="0.85"/>
      <polygon points="516,481 516,530 400,530" fill="var(--charcoal)"/>
      <polygon points="0,539 404,539 338,576 0,576" fill="var(--lime-strong)"/>
    </svg>
    <div class="brand" style="left:18px;top:402px;font-size:42px;color:var(--ink)">FERRO ASCENT</div>
    <div class="tagline" style="left:18px;top:541px">NO STRINGS ATTACHED</div>
    <div class="social">
      <span class="social__dot"></span>
      <span class="social__name">Ferro Ascent Centre</span>
    </div>
    <div class="address">7/41 Wexley Road South Tarrinbee<br>p: 9417 5836 | info@ferroascent.example.com.au</div>
    <div class="web-bar">WWW.FERROASCENT.EXAMPLE.COM.AU</div>
  </section>

</main>
</body>
</html>
```